Napa Winery Zinfandel label

We are a new start-up winery of high-end Napa wine. The label is to be silk screened or etched into the bottle. This initial logo is for the Velvet Ember Wine Co. Zinfandel wine.

The attached is an idea I would like followed for general guidance, meant to depict a "carnal sin" and sensual as per attached image.

Looking for some new ideas.....subtle sexy but risqué preferred! Silhouette in white and red writing of "Velvet zin" is what we are hoping for....

Please depict on a wine bottle (red wine) or near black background.

Thank you.

Font styles to use
Other font styles liked:
• colonna mt

Colors
f04950
ffffff

Requirements
Must have
• Female silhouette - risqué
Nice to have
• sensual - edgy
Should not have
• gold

```html
<!DOCTYPE html>
<html lang="en">
<head>
<meta charset="utf-8">
<title>Velvet Zin – Zinfandel Label</title>
<link rel="stylesheet" href="https://fonts.googleapis.com/css2?family=Saira+Condensed:wght@400;500&display=swap">
<style>
  :root {
    --bottle-black: #0d0b0c;
    --bottle-deep: #171213;
    --ink-white: #ffffff;
    --accent-red: #f04950;
    --red-deep: #6e1419;
    --etch-grey: #3d3739;
    --fine-grey: #b8b2b4;
  }
  * { margin: 0; padding: 0; box-sizing: border-box; }
  html, body {
    width: 959px;
    height: 1200px;
    overflow: hidden;
    background: var(--bottle-black);
  }
  .label {
    position: relative;
    width: 959px;
    height: 1200px;
    background: radial-gradient(ellipse at 50% 45%, var(--bottle-deep) 0%, var(--bottle-black) 70%);
    font-family: "Saira Condensed", "Arial Narrow", sans-serif;
  }
  .silhouette {
    position: absolute;
    left: 265px;
    top: 140px;
    width: 430px;
    height: 740px;
    border-radius: 48% 48% 36% 36% / 30% 30% 24% 24%;
    background: linear-gradient(180deg, var(--accent-red) 0%, #b8262e 45%, var(--red-deep) 100%);
    opacity: 0.85;
  }
  .brand-word,
  .varietal {
    position: absolute;
    color: var(--ink-white);
    font-weight: 400;
    line-height: 1;
    letter-spacing: 3px;
  }
  .brand-word {
    left: 235px;
    top: 430px;
    font-size: 170px;
  }
  .winery-name {
    position: absolute;
    left: 0;
    width: 959px;
    top: 628px;
    text-align: center;
    font-size: 22px;
    color: var(--fine-grey);
    letter-spacing: 1px;
  }
  .varietal {
    left: 400px;
    top: 675px;
    font-size: 170px;
  }
  .region,
  .vintage {
    position: absolute;
    left: 0;
    width: 959px;
    text-align: center;
    color: var(--etch-grey);
    font-weight: 500;
    line-height: 1;
  }
  .region {
    top: 915px;
    font-size: 96px;
    letter-spacing: 4px;
  }
  .vintage {
    top: 1025px;
    font-size: 60px;
    letter-spacing: 2px;
  }
</style>
</head>
<body>
  <main class="label">
    <div class="silhouette" role="img" aria-label="Red line illustration of a sensual female silhouette"></div>
    <div class="brand-word">Velvet</div>
    <div class="winery-name">Velvet Ember Wine Co.</div>
    <div class="varietal">Zin</div>
    <div class="region">Napa Valley</div>
    <div class="vintage">2015</div>
  </main>
</body>
</html>
```